Management Consulting and Executive Coaching business needs a brochure.

I need a brochure that I can send to prospective clients. I provide management consulting services and executive coaching supports targeting organizations focused on social impact. I would like to see designs that use vibrant colors consistent with my logo (see attached) and that communicate forward motion/progress.

Target Market(s)

Social Impact leaders and organizations

Industry/Entity Type

Management Consulting

Font styles to use
Serif

Colors
b29ec9
85acd3
86cae7
87d0c7
acd037

Requirements
Must have
• Must have exciting, colorful, design features using words, art, imagery.
Should not have
• No dark or depressing imagery

```html
<!DOCTYPE html>
<html lang="en">
<head>
<meta charset="utf-8">
<title>Larkspur Partnerships – Consulting Services and Coaching Supports</title>
<link href="https://fonts.googleapis.com/css2?family=Sorts+Mill+Goudy&family=Montserrat:wght@400;600;700&family=Oswald:wght@500;600;700&display=swap" rel="stylesheet">
<style>
  :root {
    --purple-deep: #4b1853;
    --purple-bullet: #4a1a52;
    --lime: #acd037;
    --magenta: #cc2a72;
    --lavender: #b29ec9;
    --blue: #2aa0cf;
    --teal: #2a9fc0;
    --white: #ffffff;
    --ink: #1e1e1e;
    --page: #f4f4f4;
  }
  * { box-sizing: border-box; margin: 0; padding: 0; }
  html, body { width: 1050px; height: 1200px; overflow: hidden; background: var(--page); }
  .flyer { position: relative; width: 1050px; height: 1200px; background: var(--white); font-family: "Montserrat", sans-serif; color: var(--ink); }

  .hero { position: absolute; left: 0; top: 0; width: 1050px; height: 549px; overflow: hidden; }
  .hero-photo { position: absolute; inset: 0;
    background: linear-gradient(180deg, #fbfbfa 0%, #eef0ec 18%, #d8dad3 40%, #a9a4a2 68%, #6c6668 100%); }

  .brand { position: absolute; top: 64px; left: 0; width: 100%; display: flex; justify-content: center; align-items: center; gap: 12px; }
  .brand-dot { width: 24px; height: 24px; border-radius: 50%; background: var(--teal); }
  .brand-name { font-family: "Montserrat", sans-serif; font-weight: 600; font-size: 26px; letter-spacing: 2px; color: var(--teal); }

  .hero-title { position: absolute; left: 292px; top: 342px; width: 379px; height: 160px;
    background: rgba(255,255,255,.72); border: 2px solid rgba(255,255,255,.95); border-radius: 14px 14px 0 0;
    font-family: "Sorts Mill Goudy", serif; font-size: 36px; line-height: 40px; text-align: center; padding-top: 18px; color: #111; }

  .url-pill { position: absolute; left: 160px; top: 496px; width: 632px; height: 53px; }
  .url-pill svg { position: absolute; inset: 0; }
  .url-pill span { position: relative; display: block; text-align: center; line-height: 53px; font-weight: 700; font-size: 27px; color: var(--white); }

  .intro { position: absolute; left: 0; top: 549px; width: 1050px; height: 222px; background: var(--purple-deep); color: var(--white); text-align: center; }
  .intro h1 { font-family: "Sorts Mill Goudy", serif; font-weight: 400; font-size: 43px; line-height: 50px; letter-spacing: 1px; margin-top: 18px; }
  .intro p { font-size: 15px; line-height: 22px; width: 750px; margin: 28px auto 0; }

  .services { position: absolute; left: 0; top: 771px; width: 1050px; height: 224px; background: var(--lime); }
  .col-left { position: absolute; left: 45px; top: 18px; width: 330px; }
  .col-right { position: absolute; left: 432px; top: 18px; width: 390px; }
  .divider { position: absolute; left: 407px; top: 22px; width: 1px; height: 180px; background: rgba(255,255,255,.6); }
  .services h2 { font-weight: 700; font-size: 18px; margin-bottom: 8px; color: #111; }
  .services h2.spaced { margin-top: 14px; }
  .services ul { list-style: none; }
  .services li { position: relative; padding-left: 20px; font-size: 15.5px; line-height: 20px; margin-bottom: 9px; color: #1b1b1b; }
  .services li::before { content: ""; position: absolute; left: 2px; top: 6px; width: 10px; height: 10px; border-radius: 50%; background: var(--purple-bullet); }
  .services li.sub { margin-left: 20px; margin-top: -3px; }

  .call-badge { position: absolute; left: 825px; top: 39px; width: 162px; height: 162px; border-radius: 50%;
    background: var(--lavender); border: 6px solid var(--white); box-shadow: 0 2px 6px rgba(0,0,0,.3);
    color: var(--white); text-align: center; font-family: "Oswald", sans-serif; font-weight: 700; padding-top: 24px; }
  .call-badge .lead { font-size: 20px; line-height: 22px; }
  .call-badge .num { font-size: 19px; margin-top: 8px; white-space: nowrap; }

  .story { position: absolute; left: 0; top: 995px; width: 1050px; height: 134px; background: var(--magenta); color: var(--white);
    font-size: 17.5px; line-height: 28px; text-align: justify; text-align-last: center; padding: 20px 54px 0 56px; }

  .footer { position: absolute; left: 0; top: 1129px; width: 1050px; height: 71px; }
  .footer svg { position: absolute; inset: 0; }
  .footer-email { position: absolute; left: 34px; top: 24px; font-size: 16px; color: var(--white); }
  .footer-email strong { font-weight: 600; }
  .footer-address { position: absolute; left: 408px; top: 14px; font-size: 16px; line-height: 23px; font-weight: 700; color: var(--white); }
  .footer-call { position: absolute; left: 670px; top: 8px; width: 370px; text-align: center; font-family: "Oswald", sans-serif; font-weight: 600; font-size: 40px; color: var(--white); }
</style>
</head>
<body>
<div class="flyer">
  <section class="hero">
    <div class="hero-photo" role="img" aria-label="Photo of a cheerful business team of five celebrating with raised arms in a bright office"></div>
    <div class="brand"><span class="brand-dot"></span><span class="brand-name">LARKSPUR PARTNERSHIPS</span></div>
    <div class="hero-title">Consulting<br>Services And<br>Coaching Supports</div>
    <div class="url-pill">
      <svg width="632" height="53" viewBox="0 0 632 53" aria-hidden="true">
        <defs><linearGradient id="pill" x1="0" y1="0" x2="0" y2="1"><stop offset="0" stop-color="#f04aa3"/><stop offset="1" stop-color="#c8167a"/></linearGradient></defs>
        <path d="M0 53 C18 53 22 0 44 0 H588 C610 0 614 53 632 53 Z" fill="url(#pill)"/>
      </svg>
      <span>www.larkspurpartnerships.com</span>
    </div>
  </section>

  <section class="intro">
    <h1>Management Consulting Services<br>And Executive Coaching Supports</h1>
    <p>We believe that high performing leaders create and lead high performing organizations. We seek to partner with leaders and organizations across sectors who share a vision and mission to make a positive impact in the community.</p>
  </section>

  <section class="services">
    <div class="col-left">
      <h2>EXECUTIVE COACHING:</h2>
      <ul>
        <li>1:1 Coaching to achieve personal and professional goals</li>
        <li>Group Coaching</li>
      </ul>
      <h2 class="spaced">MANAGEMENT CONSULTING:</h2>
      <ul>
        <li>Strategic planning,</li>
        <li>Board/executive team development,</li>
      </ul>
    </div>
    <div class="divider"></div>
    <div class="col-right">
      <ul>
        <li>Diversity training,</li>
        <li>Program development and sustainability,</li>
        <li>Management &amp; leadership training,</li>
        <li>Moderating/MC/Keynote Speaker</li>
        <li class="sub">(Topics - leadership, mission-driven philanthropy, social justice, motivational)</li>
        <li>Facilitation - retreats, team planning, analysis &amp; problem solving.</li>
      </ul>
    </div>
    <div class="call-badge">
      <div class="lead">Call Us<br>for more<br>Information</div>
      <div class="num">510-555-0148</div>
    </div>
  </section>

  <section class="story">
    Larkspur Partnerships LLc was formed based on the belief that promoting diverse perspectives leads to better solutions. The colors of the blooming larkspur represent the beauty that is created by of diverse colors. Independently, the colors are lovely, and together the colors present a spectacular and beautiful palate. We promote diversity of thought, action, and inclusion.
  </section>

  <footer class="footer">
    <svg width="1050" height="71" viewBox="0 0 1050 71" aria-hidden="true">
      <rect x="0" y="20" width="391" height="51" fill="var(--lavender)"/>
      <polygon points="391,20 400,0 660,0 660,71 391,71" fill="var(--purple-deep)"/>
      <polygon points="640,0 1050,0 1050,71 672,71" fill="var(--blue)"/>
    </svg>
    <div class="footer-email">Email: <strong>Dana@larkspurpartnerships.com</strong></div>
    <div class="footer-address">2450 Meadow Lane,<br>Oakland, CA 94610</div>
    <div class="footer-call">Call: 510-555-0148</div>
  </footer>
</div>
</body>
</html>
```